Flyer Design Project

I provide workshops for teachers, students and parents on organization - specifically laying out 3 goals, their accompanying activities and actions in 3 three hour sessions.

Please go to my website to see my brain logo. I need a flyer with the information typed below. The information may be changed and/or added to in way you see fit to better communicate the organizational intent.This is not for speech therapy clients, rather, it is for any and everyone who needs help writing out goals.

I would like the design of the flyer to reflect the concept of organization in a unique way.

http://brightvoicestudio-example.com/wp-content/uploads/2012/02/websitelogo2.jpg

ORGANIZATION

Write out your goals for the year.

How to organize your life in 3 easy steps.
Have fun organizing your life and plans.
Join a group of people dedicated to organizing all areas of life.
Complete your tasks in a fast, fun game format.
Walk away with your major goals broken down into their component parts and organize on a yearly calendar.
Three 3 hour days spent in making your life happier, less stressed and with realistic picture of what needs to be accomplished.
more effective in everything I do.
Being organized helps free our minds, enjoy relationships more, feel happier, and have greater meaning in life.

You will walk away with detailed plans for 2013.

COST: $600 for all three days.

WHO: Led by Marlene Tuvik, Cognitive Speech Therapist
WHERE: 4127 E Holm Ave
Pasco, WA 99301
509-555-0187

Requirements
Must have
• My logo from my website. A unique organized appearance.

```html
<!DOCTYPE html>
<html lang="en">
<head>
<meta charset="utf-8">
<title>Goals, Activities, Actions – Workshop Flyer</title>
<link href="https://fonts.googleapis.com/css2?family=Arimo:wght@400;700&family=Tinos:wght@700&family=Cinzel:wght@400;600&family=Roboto+Condensed:ital,wght@0,400;0,700;1,300&family=Open+Sans:wght@400;600;700&display=swap" rel="stylesheet">
<style>
  :root {
    --navy: #16166a;
    --royal: #1b3f9c;
    --sky: #2f6fc7;
    --cream: #fdf7d2;
    --gold: #f6e56a;
    --arrow-gold: #f5c51c;
    --ink: #111111;
    --heading-blue: #2b2b8f;
    --red: #d92a1f;
    --brick: #a8281a;
    --brick-dark: #7d1a10;
    --panel-line: #c9c9c9;
    --white: #ffffff;
  }
  * { margin: 0; padding: 0; box-sizing: border-box; }
  html, body { width: 868px; height: 1200px; overflow: hidden; background: var(--white); }
  .flyer { position: relative; width: 868px; height: 1200px; overflow: hidden; background: var(--white); font-family: "Arimo", Arial, sans-serif; }

  .header-band { position: absolute; left: 0; top: 0; width: 868px; height: 112px;
    background: linear-gradient(180deg, var(--white) 0%, var(--cream) 100%); }
  .header-rule { position: absolute; left: 0; top: 99px; width: 560px; height: 4px;
    background: linear-gradient(90deg, #e0703a, #3c64b8); }
  .brand { position: absolute; left: 48px; top: 28px; display: flex; align-items: center; gap: 12px; }
  .brand-dot { width: 44px; height: 44px; border-radius: 50%; background: var(--navy); }
  .brand-name { font-weight: 700; font-size: 19px; line-height: 1.15; color: var(--heading-blue); }

  .hero { position: absolute; left: 0; top: 109px; width: 868px; height: 307px;
    background: linear-gradient(90deg, var(--sky) 0%, var(--royal) 45%, var(--navy) 100%); }
  .hero-overlay { position: absolute; left: 0; top: 0; }

  .leader { position: absolute; right: 24px; top: 46px; text-align: right; color: var(--white); }
  .leader-label { font-family: "Roboto Condensed", Arial, sans-serif; font-weight: 700; font-size: 20px; }
  .leader-name { font-family: "Roboto Condensed", Arial, sans-serif; font-size: 30px; color: var(--gold); margin-top: 2px; }
  .leader-role { font-family: "Roboto Condensed", Arial, sans-serif; font-style: italic; font-weight: 300; font-size: 19px; margin-top: 4px; }

  .brain-art { position: absolute; left: 52px; top: 122px; width: 366px; height: 285px;
    border-radius: 48% 52% 44% 50% / 52% 50% 48% 46%;
    background: radial-gradient(circle at 55% 45%, #e23a1f 0%, #f08a1c 35%, #f3c11b 60%, #2a8fd6 100%); opacity: .9; }

  .step { position: absolute; right: 42px; font-family: "Tinos", "Times New Roman", serif; font-weight: 700; font-size: 42px; line-height: 48px; color: var(--white); letter-spacing: 1px; }
  .step-goals { top: 176px; }
  .step-activities { top: 243px; }
  .step-actions { top: 309px; }

  .intro-band { position: absolute; left: 0; top: 416px; width: 500px; height: 94px;
    background: linear-gradient(90deg, var(--cream) 0%, var(--white) 100%); }
  .intro-title { position: absolute; left: 24px; top: 430px; width: 400px; text-align: center;
    font-family: "Tinos", "Times New Roman", serif; font-weight: 700; font-size: 28px; line-height: 34px; color: var(--heading-blue); }

  .benefits { position: absolute; left: 24px; top: 529px; width: 425px; height: 458px;
    border: 2px solid var(--panel-line); border-radius: 8px; background: var(--white);
    box-shadow: 0 2px 6px rgba(0,0,0,.15); padding: 20px 16px 0 34px; }
  .benefits::after { content: ""; position: absolute; left: 190px; bottom: -22px;
    border-left: 20px solid transparent; border-right: 20px solid transparent; border-top: 22px solid var(--panel-line); }
  .benefit { position: relative; list-style: none; font-size: 15px; line-height: 19px; color: var(--ink); text-align: justify; margin-bottom: 19px; }
  .benefit::before { content: ""; position: absolute; left: -22px; top: 3px; width: 12px; height: 12px; border-radius: 50%;
    background: radial-gradient(circle at 35% 35%, #ff8c7a, var(--red) 60%, #8c1208); }

  .takeaway { position: absolute; left: 22px; top: 1008px; width: 427px; height: 117px; border-radius: 6px;
    background: linear-gradient(180deg, #c13a22 0%, var(--brick) 55%, var(--brick-dark) 100%);
    box-shadow: 0 2px 6px rgba(0,0,0,.3);
    display: flex; align-items: center; justify-content: center; text-align: center;
    font-family: "Cinzel", "Times New Roman", serif; font-size: 27px; line-height: 40px; color: var(--white); }
  .cost { position: absolute; left: 22px; top: 1146px; width: 427px; text-align: center; font-weight: 700; font-size: 19px; color: var(--ink); }

  .group-photo { position: absolute; left: 478px; top: 449px; width: 372px; height: 491px; border-radius: 40% 40% 30% 30%;
    background: radial-gradient(ellipse at 50% 45%, #c9a58a 0%, #d9d3c7 45%, #eeeeea 80%, var(--white) 100%); }

  .details { position: absolute; left: 480px; top: 950px; width: 394px; text-align: center; font-size: 14px; line-height: 18px; }
  .details dt { color: var(--red); font-weight: 700; }
  .details dd { color: var(--heading-blue); margin-bottom: 15px; }

  .footer-strip { position: absolute; left: 0; top: 1180px; width: 868px; height: 20px; background: linear-gradient(90deg, #2f7ad6, var(--royal)); }
  .footer-cap { position: absolute; left: 440px; top: 1108px; }
  .contact { position: absolute; right: 28px; top: 1126px; text-align: right; color: var(--white); font-family: "Open Sans", Arial, sans-serif; }
  .contact-address { font-size: 16px; }
  .contact-call { font-size: 19px; margin-top: 4px; }
  .contact-phone { font-size: 30px; font-weight: 700; margin-left: 6px; vertical-align: -3px; }
</style>
</head>
<body>
<main class="flyer">
  <div class="header-band"></div>
  <div class="header-rule"></div>
  <div class="brand">
    <span class="brand-dot"></span>
    <span class="brand-name">The Bright Voice<br>Learning Studio</span>
  </div>

  <section class="hero"></section>

  <div class="brain-art" role="img" aria-label="Illustration of a brain made of colourful interlocking gears"></div>

  <svg class="hero-overlay" width="868" height="420" viewBox="0 0 868 420" aria-hidden="true">
    <path d="M560 112 C600 112 610 36 660 36 H868 V112 Z" fill="var(--navy)"/>
    <g stroke="var(--arrow-gold)" stroke-width="3" fill="none">
      <polyline points="196,175 218,200 628,200"/>
      <polyline points="227,268 240,265 527,265"/>
      <polyline points="197,354 218,326 563,326"/>
    </g>
    <g fill="var(--arrow-gold)">
      <path d="M626 188 L638 200 L626 212 Z"/>
      <path d="M525 253 L537 265 L525 277 Z"/>
      <path d="M561 314 L573 326 L561 338 Z"/>
    </g>
    <g fill="var(--white)">
      <circle cx="196" cy="175" r="14"/>
      <circle cx="227" cy="268" r="14"/>
      <circle cx="197" cy="354" r="14"/>
    </g>
  </svg>

  <div class="leader">
    <div class="leader-label">Program Led by</div>
    <div class="leader-name">Marlene Tuvik</div>
    <div class="leader-role">Cognitive Speech Therapist</div>
  </div>

  <div class="step step-goals">GOALS</div>
  <div class="step step-activities">ACTIVITIES</div>
  <div class="step step-actions">ACTIONS</div>

  <div class="intro-band"></div>
  <h1 class="intro-title">WRITE OUT YOUR<br>GOALS FOR THE YEAR</h1>

  <ul class="benefits">
    <li class="benefit">ORGANIZATION!<br>Spend 3-hour sessions making your life less stressed and creating a realistic picture of what needs to be accomplished.</li>
    <li class="benefit">Become more effective in everything you do so you have more time for the things important to you.</li>
    <li class="benefit">Walk away with your major goals broken down into their component parts and organized on a yearly calendar.</li>
    <li class="benefit">Complete your tasks in a fast, fun game format.?</li>
    <li class="benefit">Join a group of people dedicated to organizing all areas of life and tap into their support.</li>
    <li class="benefit">Have fun organizing your life and plans.</li>
    <li class="benefit">Being organized helps free our minds, enjoy relationships more, feel happier, and have greater meaning in life.</li>
  </ul>

  <div class="takeaway">You will walk away with<br>detailed plans for 2013</div>
  <p class="cost">COST: $600 for all three days</p>

  <div class="group-photo" role="img" aria-label="Photo of a smiling group of adults giving thumbs up"></div>

  <dl class="details">
    <dt>WHO:</dt>
    <dd>Adults of any age including high school and<br>college students ready to develop a plan for your life.</dd>
    <dt>WHEN:</dt>
    <dd>February 9, 16, 23 of 2013 9 a.m. to 12 p.m.</dd>
    <dt>INVESTMENT:</dt>
    <dd>$597</dd>
  </dl>

  <div class="footer-strip"></div>
  <svg class="footer-cap" width="428" height="92" viewBox="0 0 428 92" aria-hidden="true">
    <path d="M0 92 C40 92 50 0 110 0 H428 V92 Z" fill="var(--navy)"/>
  </svg>
  <div class="contact">
    <div class="contact-address">4127 E Holm Ave., Pasco, WA 99301</div>
    <div class="contact-call">Call Us today<span class="contact-phone">509-555-0187</span></div>
  </div>
</main>
</body>
</html>
```